BUSINESS CARD needed for TRAVEL BUSINESS

-Background-

Wandorvist Crew (WC) is a newly found company in Asia that trains and develops people with various demographics to become a FREQUENT TRAVELER & an ENTREPRENEUR combined. Basically, the core product that the company markets teaches people how to TRAVEL leisurely and yet EARN MONEY at the same time. Our main quote will be WANDER WIDE, EARN MORE.

- The Job -

We will be constantly going out to different events, whether opening promotional booths in roadshows or at colleges or going for networking events. Thus we need a BUSINESS CARD design that portrays our POSITIONING & BRANDING

- Positioning -

TRAVEL LEISURELY & EARN at the SAME TIME

- Objective -

Serve as a BTL marketing & networking tool

- Target Audience -

Male & Females aged 19 - 35 who LOVES to TRAVEL & have strong aspirations to make it big and attaining financial freedom. The audience are enthusiastic and when they see an opportunity, they will seize it on the very spot. They are well connected and have a wide social network.

- Single Minded Proposition -

WC is My Dream Life

Target Market(s)

REFER TO CREATIVE BRIEF

Industry/Entity Type

Marketing

Requirements
Must have
• 1) The business card must portray a branding thats related to TRAVEL.

Boarding pass design was what we came up with but express your creativity and surprise me with better ideas. :)
Nice to have
• This is an idea that we have and we would most likely like to use however I do not want to restrict your creativity so i am putting in NICE TO HAVE instead.

Our idea design -> To have the namecard in the format of a BOARDING PASS lookalike

(You may refer to these weblink for inspiration -> https://www.pictofind.example/search?hl=en&q=boarding+pass&bav=on.2,or.r_gc.r_pw.r_cp.r_qf.,cf.osb&biw=1366&bih=667&um=1&ie=UTF-8&tbm=isch&source=og&sa=N&tab=wi&ei=l-f9T4KqC4fWrQfx8eC-Bg

or simply PICTOFIND BOARDING PASS IMAGES

```html
<!DOCTYPE html>
<html lang="en">
<head>
<meta charset="utf-8">
<title>Wandorvist Crew – Business Card</title>
<link rel="stylesheet" href="https://fonts.googleapis.com/css2?family=Roboto+Condensed:wght@700&family=Arvo&family=Open+Sans:wght@700&display=swap">
<style>
  :root {
    --brand-blue: #233f94;
    --ink: #111111;
    --label-grey: #6d6d6d;
    --paper: #f1f1f1;
    --paper-shade: #e2e2e2;
    --stripe: #0d0d0d;
    --backdrop: #e7e4df;
    --art-blue: #8ea0cf;
  }
  * { margin: 0; padding: 0; box-sizing: border-box; }
  html, body { width: 1200px; height: 989px; overflow: hidden; }
  body { background: var(--backdrop); position: relative; font-family: "Open Sans", sans-serif; }

  .card {
    position: absolute;
    top: 63px;
    width: 490px;
    height: 862px;
    border-radius: 26px;
    overflow: hidden;
    background: radial-gradient(ellipse at 40% 40%, var(--paper) 0%, var(--paper) 55%, var(--paper-shade) 100%);
  }
  .card--front { left: 80px; }
  .card--back  { left: 629px; }

  /* Front */
  .front-art {
    position: absolute;
    left: 23px; top: 80px;
    width: 445px; height: 254px;
    background: linear-gradient(160deg, var(--art-blue), var(--brand-blue));
    border-radius: 6px;
    opacity: .85;
  }
  .front-brand {
    position: absolute;
    left: 0; right: 18px; top: 402px;
    text-align: right;
    font-family: "Roboto Condensed", sans-serif;
    font-weight: 700;
    font-size: 58px;
    line-height: 1;
    color: var(--brand-blue);
    letter-spacing: -1px;
  }
  .front-tagline {
    position: absolute;
    right: 18px; top: 464px;
    font-family: "Open Sans", sans-serif;
    font-weight: 700;
    font-size: 15px;
    letter-spacing: 3.6px;
    color: var(--label-grey);
    opacity: .8;
    white-space: nowrap;
  }
  .front-offer {
    position: absolute;
    left: 0; right: 0; top: 756px;
    text-align: center;
    font-family: "Open Sans", sans-serif;
    font-weight: 700;
    font-size: 23px;
    letter-spacing: 4px;
    color: var(--brand-blue);
  }
  .front-pointer { position: absolute; left: 190px; top: 790px; }

  /* Back */
  .mag-stripe {
    position: absolute;
    left: 21px; top: 0;
    width: 86px; height: 100%;
    background: var(--stripe);
  }
  .back-brand {
    position: absolute;
    left: 121px; top: 26px;
    font-family: "Roboto Condensed", sans-serif;
    font-weight: 700;
    font-size: 44px;
    line-height: 1;
    color: var(--brand-blue);
    letter-spacing: -0.5px;
  }
  .details { position: absolute; left: 116px; top: 105px; width: 350px; list-style: none; }
  .detail {
    position: relative;
    height: 93.5px;
    padding-left: 13px;
    padding-top: 4px;
  }
  .detail__label {
    display: block;
    font-size: 13px;
    font-weight: 700;
    color: var(--label-grey);
    letter-spacing: .2px;
  }
  .detail__value {
    display: block;
    margin-top: 4px;
    font-family: "Arvo", serif;
    font-size: 22px;
    color: var(--ink);
    white-space: nowrap;
  }
  .detail__value--name { font-size: 28px; margin-top: 0; letter-spacing: .5px; }
  .detail::after {
    content: "";
    position: absolute;
    left: 0; right: 0; bottom: 28px;
    height: 7px;
    border-bottom: 2px solid var(--brand-blue);
    border-right: 2px solid var(--brand-blue);
  }

  .back-art {
    position: absolute;
    left: 113px; top: 658px;
    width: 358px; height: 172px;
    background: linear-gradient(180deg, #c3cbe4, var(--art-blue));
    border-radius: 6px;
    opacity: .85;
  }
  .motto-pill {
    position: absolute;
    left: 178px; top: 827px;
    width: 224px; height: 24px;
    border-radius: 50% 50% 10px 10px / 60% 60% 10px 10px;
    background: var(--brand-blue);
    color: #ffffff;
    font-size: 13px;
    font-weight: 700;
    letter-spacing: .6px;
    text-align: center;
    line-height: 26px;
    white-space: nowrap;
  }
</style>
</head>
<body>

  <section class="card card--front" aria-label="Business card front">
    <div class="front-art" role="img" aria-label="Silhouette of an airliner taking off"></div>
    <h1 class="front-brand">Wandorvist Crew</h1>
    <p class="front-tagline">WANDER WIDE, EARN MORE</p>
    <p class="front-offer">TRAVEL &amp; EARN</p>
    <svg class="front-pointer" width="112" height="54" viewBox="0 0 112 54" aria-hidden="true">
      <polygon points="0,0 112,0 56,54" fill="var(--brand-blue)"/>
    </svg>
  </section>

  <section class="card card--back" aria-label="Business card back">
    <div class="mag-stripe"></div>
    <h2 class="back-brand">Wandorvist Crew</h2>
    <ul class="details">
      <li class="detail"><span class="detail__label">NAME</span><span class="detail__value detail__value--name">MARA TENZEL</span></li>
      <li class="detail"><span class="detail__label">CONTACT NUMBER</span><span class="detail__value">+65 8127 4096</span></li>
      <li class="detail"><span class="detail__label">EMAIL</span><span class="detail__value">mara.t@postvale.example</span></li>
      <li class="detail"><span class="detail__label">WEBSITE</span><span class="detail__value">wandorvistcrew.example</span></li>
      <li class="detail"><span class="detail__label">SOCIAL</span><span class="detail__value">sc.example/WandorvistCrew</span></li>
      <li class="detail"><span class="detail__label">CHAT ID</span><span class="detail__value">maratenzel90</span></li>
    </ul>
    <div class="back-art" role="img" aria-label="Two palm trees with a hammock slung between them"></div>
    <p class="motto-pill">WANDER WIDE, EARN MORE</p>
  </section>

</body>
</html>
```